BPR Business Card

We need a business card that reflect our business, we have put anther business card as an example of what we like but please feel free to do your own thing.

Here are the items to be placed on card

Glen Harwick
Bright Parcel Route
Mobile: 917-555-4862
Office: 516-555-7104
Fax: 866-555-3927
Email: info@brightparcelroute.example
Website: brightparcelroute.example

I have added raw files to upload

Glen Harwick
Bright Parcel Route
Mobile: 917-555-4862
Office: 516-555-7104
Fax: 866-555-3927 

Target Market(s)

Natural product manufactures, and retailers and distributors

Industry/Entity Type

Business

Requirements
Must have
• 1. Logo
2. The colors of the company

```html
<!DOCTYPE html>
<html lang="en">
<head>
<meta charset="utf-8">
<title>Bright Parcel Route – Business Card</title>
<link href="https://fonts.googleapis.com/css2?family=Fredoka:wght@600&family=Great+Vibes&family=Open+Sans:wght@400&family=Oswald:wght@600&display=swap" rel="stylesheet">
<style>
  :root {
    --brand-green: #6cb443;
    --panel-dark: #2a2a2a;
    --paper: #ffffff;
    --tint: #eef3ea;
    --ink: #111111;
    --trim: #e8287a;
    --safe: #3a6fb0;
    --bleed: #e29a4c;
  }
  html, body { margin: 0; padding: 0; overflow: hidden; background: var(--paper); }
  .card {
    position: relative; width: 1200px; height: 720px; overflow: hidden;
    background: var(--paper);
    font-family: "Fredoka", sans-serif;
  }
  .pattern-zone { position: absolute; left: 0; top: 0; width: 605px; height: 720px; background: var(--tint); }
  .green-field { position: absolute; left: 605px; top: 0; right: 0; bottom: 0;
    background: radial-gradient(circle at 75% 70%, #7cc24f 0%, var(--brand-green) 55%); }
  .guide { position: absolute; box-sizing: border-box; pointer-events: none; }
  .guide--bleed { left: 2px; top: 2px; right: 2px; bottom: 2px; border: 1.5px dashed var(--bleed); }
  .guide--trim { left: 40px; top: 40px; width: 1121px; height: 639px; border: 2px solid var(--trim); }
  .guide--safe { left: 80px; top: 80px; width: 1039px; height: 559px; border: 1.5px dashed var(--safe); }

  .panel { position: absolute; left: 43px; top: 119px; width: 562px; height: 450px;
    background: var(--panel-dark); border-radius: 32px 0 0 32px; }
  .tab { position: absolute; left: 605px; width: 115px; background: var(--panel-dark);
    border-radius: 0 18px 18px 0; }
  .icon { position: absolute; left: 652px; width: 60px; height: 60px; }

  .name { position: absolute; left: 92px; width: 520px; top: 145px; text-align: center;
    font-family: "Great Vibes", cursive; font-size: 74px; line-height: 1; color: var(--paper); }
  .company { position: absolute; left: 160px; width: 480px; top: 226px; text-align: center;
    font-family: "Open Sans", sans-serif; font-size: 29px; line-height: 1.1; color: var(--paper); }

  .brand { position: absolute; left: 80px; width: 560px; top: 398px; display: flex;
    align-items: center; justify-content: center; gap: 16px; }
  .brand__mark { width: 40px; height: 40px; background: var(--brand-green); }
  .brand__name { font-family: "Fredoka", sans-serif; font-weight: 600; font-size: 42px;
    color: var(--brand-green); white-space: nowrap; }

  .contact { position: absolute; left: 728px; color: var(--ink); font-weight: 600;
    white-space: nowrap; transform: translateY(-50%); line-height: 1; }
  .contact--phone { font-size: 40px; letter-spacing: 0.5px; }
  .contact--email { font-size: 19px; letter-spacing: 0.8px; text-transform: uppercase; }
  .contact--web { font-size: 21px; letter-spacing: 0.8px; text-transform: uppercase; }
  .address { position: absolute; left: 627px; top: 574px; font-family: "Oswald", sans-serif;
    font-weight: 600; font-size: 28px; color: var(--paper); white-space: nowrap; letter-spacing: 0.3px; }
</style>
</head>
<body>
<div class="card">
  <div class="pattern-zone" role="img" aria-label="Faint repeated company name pattern"></div>
  <div class="green-field"></div>

  <div class="panel"></div>
  <div class="tab" style="top:119px;height:79px"></div>
  <div class="tab" style="top:210px;height:78px"></div>
  <div class="tab" style="top:300px;height:77px"></div>
  <div class="tab" style="top:391px;height:78px"></div>
  <div class="tab" style="top:489px;height:80px"></div>

  <!-- mobile -->
  <svg class="icon" style="top:128px" viewBox="0 0 60 60">
    <circle cx="30" cy="30" r="27" fill="none" stroke="var(--brand-green)" stroke-width="3"/>
    <rect x="22" y="13" width="16" height="34" rx="3" fill="none" stroke="#fff" stroke-width="2.5"/>
    <rect x="25" y="18" width="10" height="10" fill="#fff"/>
    <circle cx="30" cy="40" r="2" fill="#fff"/>
  </svg>
  <!-- office phone -->
  <svg class="icon" style="top:219px" viewBox="0 0 60 60">
    <circle cx="30" cy="30" r="27" fill="none" stroke="var(--brand-green)" stroke-width="3"/>
    <path d="M14 24 Q30 12 46 24 L42 29 L37 26 L37 22 Q30 20 23 22 L23 26 L18 29 Z" fill="#fff"/>
    <path d="M20 30 L40 30 L44 44 L16 44 Z" fill="#fff"/>
    <circle cx="30" cy="37" r="4" fill="var(--panel-dark)"/>
  </svg>
  <!-- fax -->
  <svg class="icon" style="top:307px" viewBox="0 0 60 60">
    <circle cx="30" cy="30" r="27" fill="none" stroke="var(--brand-green)" stroke-width="3"/>
    <rect x="22" y="13" width="16" height="16" fill="none" stroke="#fff" stroke-width="2"/>
    <line x1="25" y1="18" x2="35" y2="18" stroke="#fff" stroke-width="1.5"/>
    <line x1="25" y1="22" x2="35" y2="22" stroke="#fff" stroke-width="1.5"/>
    <rect x="15" y="29" width="30" height="16" rx="2" fill="none" stroke="#fff" stroke-width="2.5"/>
    <line x1="20" y1="38" x2="40" y2="38" stroke="#fff" stroke-width="2"/>
  </svg>
  <!-- email -->
  <svg class="icon" style="top:400px" viewBox="0 0 60 60">
    <circle cx="30" cy="30" r="27" fill="none" stroke="var(--brand-green)" stroke-width="3"/>
    <rect x="15" y="19" width="30" height="22" fill="none" stroke="#fff" stroke-width="2.5"/>
    <path d="M15 19 L30 32 L45 19" fill="none" stroke="#fff" stroke-width="2.5"/>
  </svg>
  <!-- web -->
  <svg class="icon" style="top:499px" viewBox="0 0 60 60">
    <circle cx="30" cy="30" r="27" fill="none" stroke="var(--brand-green)" stroke-width="3"/>
    <circle cx="30" cy="30" r="15" fill="none" stroke="#fff" stroke-width="2.5"/>
    <ellipse cx="30" cy="30" rx="6" ry="15" fill="none" stroke="#fff" stroke-width="2"/>
    <line x1="15" y1="30" x2="45" y2="30" stroke="#fff" stroke-width="2"/>
    <line x1="18" y1="22" x2="42" y2="22" stroke="#fff" stroke-width="1.8"/>
    <line x1="18" y1="38" x2="42" y2="38" stroke="#fff" stroke-width="1.8"/>
  </svg>

  <div class="name">Glen Harwick</div>
  <div class="company">Bright Parcel Route</div>

  <div class="brand">
    <span class="brand__mark"></span>
    <span class="brand__name">Bright Parcel Route</span>
  </div>

  <div class="contact contact--phone" style="top:163px">917-555-4862</div>
  <div class="contact contact--phone" style="top:254px">516-555-7104</div>
  <div class="contact contact--phone" style="top:337px">866-555-3927</div>
  <div class="contact contact--email" style="top:430px">info@brightparcelroute.example</div>
  <div class="contact contact--web" style="top:531px">brightparcelroute.example</div>
  <div class="address">218 ALDER COURT, LINDENVALE, ST 00000</div>

  <div class="guide guide--bleed"></div>
  <div class="guide guide--trim"></div>
  <div class="guide guide--safe"></div>
</div>
</body>
</html>
```